Where Quiet Rivers Carry Us

I have a previously designed book cover, and although I am mostly happy with it, I do not care for the photo on the cover of the book. I would like to keep the fonts and scrollwork on the current book cover (the brown outer edge is optional).
I prefer a Christian focus with a soft, gentle, grieving, trusting feeling of a mother as God leads without the typical religious symbols (ie: huge hands, overwhelming crosses, Heaven opening). Softly toned or small Christian icons would be acceptable.
The book dimensions are 5.5 X 8.5 and the spine is 1/2" thick.
Original book cover is here: http://wherequietriverscarryus.pinebrookpages.net/p/free-books.html
Back cover book description (two photos and the logo for the back cover can be found below) :
For I am the Lord your God who takes hold of your right hand and says to you, "Do not fear, I will help you." Isaiah 41:13
One day you were here, Colby, the next you were at the throne of God. How I long to know what heaven is like so I can envision where you are. Are you talking to Gideon about the battles of old? Are you asking Paul about the stonings, the scales, and the shipwrecks? Or are you still just standing in awe of the God and Savior that your mother could never have come close to describing to you? How I long to stand in awe with you, praising the God who gives and takes away. Just like I told you all those times when you were here with us, "If you go first, I'll see you when I get there, my son." Love you, Mom
On Friday, February 18, 2011, God did the unthinkable in our lives: He chose to take our 12-year-old son, Colby, home to heaven in a skiing accident. It is only considered the unthinkable because our plans are not God's plans and our ways are not God's ways. Follow along on my journey through the valley of the shadow of death as my Savior, Jesus Christ, leads me.
(Author info)
Janna L. Voskuilen lives on a small farm in northern Wisconsin with her husband, Dale, and their children. Experiencing the tragic death of her son has caused her to draw closer to God as He leads her down an unexpected path to know Him better.
I have updated the back cover details to include the exact words for the back cover as well as two photos and a logo. Thank you, designers, for sharing your creativity!
Reason: Still looking for the perfect book cover!
Reason: Still looking for the perfect design!
Working on final revisions!

```html
<!DOCTYPE html>
<html lang="en">
<head>
<meta charset="utf-8">
<title>Where Quiet Rivers Carry Us — Book Cover</title>
<link href="https://fonts.googleapis.com/css2?family=Pinyon+Script&family=Cinzel:wght@600;700&family=EB+Garamond:ital,wght@0,400;0,600;0,700;1,400&display=swap" rel="stylesheet">
<style>
  :root {
    --parchment-light: #f6e3a6;
    --parchment-mid: #eccf7d;
    --parchment-warm: #e2b25a;
    --parchment-edge: #c98a3a;
    --ink: #1b1208;
    --ink-soft: #2c2012;
    --photo-sepia: #8a7a52;
    --photo-dark: #4a3d28;
  }
  * { box-sizing: border-box; margin: 0; padding: 0; }
  html, body { width: 1200px; height: 894px; overflow: hidden; background: #ffffff; }
  .cover {
    position: relative;
    width: 1200px;
    height: 894px;
    overflow: hidden;
    color: var(--ink);
    font-family: "EB Garamond", Georgia, serif;
    background:
      radial-gradient(ellipse 55% 60% at 72% 55%, var(--parchment-light) 0%, rgba(246,227,166,0) 70%),
      radial-gradient(ellipse 45% 55% at 28% 55%, var(--parchment-light) 0%, rgba(246,227,166,0) 75%),
      radial-gradient(ellipse 80% 80% at 50% 50%, var(--parchment-mid) 40%, var(--parchment-warm) 80%, var(--parchment-edge) 100%);
  }

  /* ---------- Back cover ---------- */
  .back-quote {
    position: absolute;
    left: 36px; top: 144px; width: 520px;
    text-align: center;
    font-size: 17px;
    line-height: 21px;
  }
  .back-quote strong { font-weight: 700; }
  .child-photo {
    position: absolute;
    left: 219px; top: 241px; width: 126px; height: 147px;
    background: linear-gradient(160deg, var(--photo-sepia), var(--photo-dark));
  }
  .back-intro {
    position: absolute;
    left: 46px; top: 405px; width: 466px;
    text-align: center;
    font-size: 15px;
    line-height: 18.5px;
  }
  .back-intro .date { font-weight: 700; }
  .back-letter {
    position: absolute;
    left: 48px; top: 538px; width: 494px;
    font-size: 14.2px;
    line-height: 18.2px;
  }
  .photo-offset {
    float: left;
    width: 0;
    height: 52px;
  }
  .author-photo {
    float: left;
    clear: left;
    width: 154px; height: 203px;
    margin: 0 8px 4px -17px;
    background: linear-gradient(170deg, #6b6150, #2a241b);
  }
  .author-bio { margin-top: 6px; }

  /* ---------- Spine ---------- */
  .spine-title, .spine-author {
    position: absolute;
    writing-mode: vertical-rl;
    font-family: "EB Garamond", Georgia, serif;
    text-transform: uppercase;
    font-size: 20px;
    letter-spacing: 0.5px;
    white-space: nowrap;
    color: var(--ink);
  }
  .spine-title { left: 565px; top: 68px; }
  .spine-author { left: 565px; top: 468px; }
  .spine-imprint {
    position: absolute;
    left: 568px; top: 748px; width: 26px;
    display: flex; flex-direction: column; align-items: center; gap: 6px;
  }
  .spine-imprint .imprint-mark {
    width: 10px; height: 10px;
    background: var(--ink);
  }
  .spine-imprint .imprint-name {
    writing-mode: vertical-rl;
    font-family: "EB Garamond", Georgia, serif;
    font-weight: 400;
    font-size: 11px;
    white-space: nowrap;
    color: var(--ink);
  }

  /* ---------- Front cover ---------- */
  .front-title {
    position: absolute;
    left: 650px; top: 190px; width: 490px;
    color: var(--ink);
  }
  .front-title .script {
    display: block;
    font-family: "Pinyon Script", cursive;
    font-weight: 400;
    font-size: 92px;
    line-height: 100px;
  }
  .front-title .script.lead { padding-left: 6px; }
  .front-title .script.tail { text-align: right; padding-right: 10px; margin-top: -12px; }
  .front-title .caps {
    display: block;
    font-family: "Cinzel", serif;
    font-weight: 700;
    font-size: 64px;
    line-height: 58px;
    letter-spacing: 1px;
    padding-left: 30px;
    margin-top: -6px;
  }
  .title-flourish {
    position: absolute;
    left: 655px; top: 445px; width: 455px; height: 48px;
  }
  .front-author {
    position: absolute;
    left: 650px; top: 494px; width: 490px;
    text-align: center;
    font-family: "EB Garamond", Georgia, serif;
    font-size: 30px;
    letter-spacing: 1px;
    text-transform: uppercase;
  }
</style>
</head>
<body>
<main class="cover">

  <section class="back-cover">
    <p class="back-quote">
      For I am the Lord your God who takes hold of your right hand<br>
      and says to you,<br>
      <strong>"Do not fear, I will help you."</strong><br>
      Isaiah 41:13
    </p>

    <div class="child-photo" role="img" aria-label="Sepia portrait photograph of the author's son Colby"></div>

    <p class="back-intro">
      <span class="date">On Friday, February 18, 2011,</span><br>
      God did the unthinkable in our lives:<br>
      He chose to take our 12-year-old son, Colby, home to heaven in a skiing accident. It is only considered the unthinkable because our plans are not God's plans and our ways are not God's ways. Follow along on my journey through the valley of the shadow of death as my Savior, Jesus Christ, leads me.
    </p>

    <div class="back-letter">
      <div class="photo-offset"></div>
      <div class="author-photo" role="img" aria-label="Black and white portrait photograph of author Janna L. Voskuilen"></div>
      <p class="letter-text">One day you were here, Colby, the next you were at the throne of God. How I long to know what heaven is like so I can envision where you are. Are you talking to Gideon about the battles of old? Are you asking Paul about the stonings, the scales, and the shipwrecks? Or are you still just standing in awe of the God and Savior that your mother could never have come close to describing to you? How I long to stand in awe with you, praising the God who gives and takes away. Just like I told you all those times when you were here with us, "If you go first, I'll see you when I get there, my son." Love you, Mom</p>
      <p class="author-bio">Janna L. Voskuilen lives on a small farm in northern Wisconsin with her husband, Dale, and their children. Experiencing the tragic death of her son has caused her to draw closer to God as He leads her down an unexpected path to know Him better.</p>
    </div>
  </section>

  <section class="spine">
    <h2 class="spine-title">Where Quiet Rivers Carry Us</h2>
    <p class="spine-author">Janna L. Voskuilen</p>
    <div class="spine-imprint">
      <span class="imprint-mark"></span>
      <span class="imprint-name">Stillwater Hill Press</span>
    </div>
  </section>

  <section class="front-cover">
    <h1 class="front-title">
      <span class="script lead">Where Quiet</span>
      <span class="caps">RIVERS</span>
      <span class="script tail">Carry Us</span>
    </h1>
    <svg class="title-flourish" viewBox="0 0 455 48" role="img" aria-label="Decorative scrollwork flourish beneath the title">
      <rect x="0" y="10" width="455" height="28" rx="14" fill="#1b1208" opacity="0.12"/>
    </svg>
    <p class="front-author">Janna L. Voskuilen</p>
  </section>

</main>
</body>
</html>
```